Australian Painting company requires DL Flyer to help grow business

We need a flyer to post, email and leave with clients which details our company information and identifies the services we provide

Needs to incorporate our existing logo and show photos which will be provided when basic layout and designer is chosen

my mistake for not making the brief clear earlier; I would like an A4 double sided flyer which folds to DL

Target Market(s)

property managers, facility managers, property owners

Industry/Entity Type

Business

Requirements
Must have
• Company Name - Bellwick Paintworks Australia
Phone Number - 1300 842 306
Web Address - www.bpwks.com.au
Email: admin@bpwks.com.au
Facebook symbol
Twitter symbol
Logo - Attached to brief
Description of services;
◾External Painting
◾Internal Painting
◾Texture Coating
◾Two Pak Epoxy products
◾Line marking
◾Epoxy floors and walkways
◾Waterproofing
◾Roof Painting
◾Handyman Services
◾Rope Access Painting
◾Maintenance Programmes
◾Painting Project Management
◾Prestigious Home Painting
Nice to have
• Photos of some projects; some photos are attached
can provide more when a design is selected
Should not have
• Too much information - needs to be easy to read

```html
<!DOCTYPE html>
<html lang="en">
<head>
<meta charset="utf-8">
<title>Bellwick Paintworks Australia – Services</title>
<link rel="stylesheet" href="https://fonts.googleapis.com/css2?family=Arimo:wght@400&display=swap">
<style>
  :root {
    --blue-light: #1ea6e6;
    --blue-mid: #1a78cc;
    --blue-deep: #17389a;
    --swoosh: rgba(255, 255, 255, 0.08);
    --text: #ffffff;
    --photo-border: #f4f4f4;
    --floor-warm: #b5532a;
    --floor-deep: #7a2a14;
    --floor-gold: #e3a049;
    --house-sky: #d7dde3;
    --house-green: #3f7a5a;
    --house-brick: #8a4a3a;
    --house-lawn: #4f8a3c;
  }
  html, body {
    margin: 0;
    padding: 0;
    overflow: hidden;
  }
  .flyer-panel {
    position: relative;
    width: 1132px;
    height: 1200px;
    overflow: hidden;
    background: linear-gradient(100deg, var(--blue-light) 0%, var(--blue-mid) 50%, var(--blue-deep) 100%);
    font-family: "Arimo", Arial, sans-serif;
    color: var(--text);
  }
  .swoosh {
    position: absolute;
    inset: 0;
    width: 100%;
    height: 100%;
  }
  .service-list {
    position: absolute;
    margin: 0;
    padding: 0;
    list-style: none;
    font-size: 30px;
    line-height: 41px;
  }
  .service-list li {
    position: relative;
    padding-left: 66px;
    white-space: nowrap;
  }
  .service-list li::before {
    content: "";
    position: absolute;
    left: 0;
    top: 18px;
    width: 8px;
    height: 8px;
    border-radius: 50%;
    background: var(--text);
  }
  .service-list--top {
    left: 40px;
    top: 24px;
  }
  .service-list--bottom {
    left: 586px;
    top: 922px;
  }
  .project-photo {
    position: absolute;
    box-sizing: border-box;
    border: 8px solid var(--photo-border);
    box-shadow: 6px 10px 22px rgba(0, 0, 0, 0.45);
  }
  .project-photo--floor {
    left: 566px;
    top: 103px;
    width: 532px;
    height: 479px;
    transform: rotate(7.6deg);
    background:
      radial-gradient(circle at 42% 34%, var(--floor-gold) 0%, rgba(227, 160, 73, 0.6) 14%, transparent 40%),
      linear-gradient(160deg, var(--floor-warm) 0%, #a14422 55%, var(--floor-deep) 100%);
  }
  .project-photo--house {
    left: 45px;
    top: 485px;
    width: 705px;
    height: 469px;
    transform: rotate(-5.4deg);
    background:
      linear-gradient(180deg, var(--house-sky) 0%, #c3ccd3 18%, var(--house-green) 30%, #356a4d 62%, var(--house-brick) 72%, var(--house-lawn) 82%, #3c6f2e 100%);
  }
</style>
</head>
<body>
  <main class="flyer-panel">
    <svg class="swoosh" viewBox="0 0 1132 1200" aria-hidden="true">
      <path d="M-40 1150 C 220 620, 700 360, 1180 300 L 1180 380 C 760 430, 300 700, 40 1200 Z" fill="var(--swoosh)"/>
      <path d="M360 1200 C 520 900, 820 700, 1180 640 L 1180 700 C 860 760, 600 930, 460 1200 Z" fill="var(--swoosh)"/>
    </svg>

    <ul class="service-list service-list--top">
      <li>External Painting</li>
      <li>Internal Painting</li>
      <li>Texture Coating</li>
      <li>Two Pak Epoxy products</li>
      <li>Line Marking</li>
      <li>Epoxy floors and walkways</li>
      <li>Waterproofing</li>
    </ul>

    <div class="project-photo project-photo--floor" role="img" aria-label="Project photo: glossy terracotta epoxy floor with a golden sun motif inlay"></div>
    <div class="project-photo project-photo--house" role="img" aria-label="Project photo: freshly painted green two-storey house with white trim, red front door and garden"></div>

    <ul class="service-list service-list--bottom">
      <li>Roof Painting</li>
      <li>Handyman Services</li>
      <li>Rope Access Painting</li>
      <li>Maintenance Programmes</li>
      <li>Painting Project Management</li>
      <li>Prestigious Home Painting</li>
    </ul>
  </main>
</body>
</html>
```